House Cleaning Website - Maid Services

Logo, landing page design with contact form - coded MUST BE MOBILE FRIENDLY

Cleaning business - maid service - i've added a few example websites

Clean, Smart Website Design that is built for getting leads

CONTENT FOR HOME PAGE -

Cleaning Seminole County Homes For Over 12 Years

Renata Sweeps

* Trusted by your neighbors for more than a decade
* Affordable and flexible to accommodate your needs
* 200% Money Back Guarantee
* Up to 20% Discount on Continued Cleanings
* Same Day Cleanings

My Clients Are Happy
"Renata has been cleaning my home for the past 3 1/2 years and I couldn't be happier with her. I trust her with cleaning my home while I'm out of town and recommend her to my friends."

Target Market(s)

people looking for house cleaning

Industry/Entity Type

Cleaning Service

Contact Information for Business Card

Renata Sweeps -
#555-318-0264
200% Guarantee
on back of card - $25 Referral Fee

Logo Text

Renata Sweeps

Coding

Coded - Design and coding required

Number of Pages Required

3 page

Requirements
Must have
• 4 links in top toolbar - services, contact, free estimate and about
• *contact will be a popup form to contact
• *services will be a graphic similar to the one on this page ... https://www.brightnestcrew.com/maid-services/
• *free estimate link will be a page with same questions as
• Must have landing page concept - I will be advertising to get people to submit their information...
• 1. Must have a "Request FREE Estimate" button that pops up a box for them to submit their information - name, number, email. Once they submit this information, they will be taken to a 2nd form to complete their details - If they dont complete the 2nd part I still receive the 1st part to call. The 2nd part will have same questions ashttps://www.tidyhearthco.com/local-house-cleaning/fl/west-miami/request-a-cleaning.aspx?cpgnId=FE0CA3B4-3A4C-4D9C-9B11-E69492B42092&scid=3554195&cid=2303288&tc=17072613580054989&rl_key=a0563857ec931d2a952e39d66a08939d&kw=77903:7716&pub_cr_id=200261568213&dynamic_proxy=1&primary_serv=www.tidyhearthco.com&rl_track_landing_pages=1
• 2. Must have pricing like https://www.brightnestcrew.com/ 1 bedroom through 6 bedroom pricing base pricing graphic.
• 2.Must have a 200% satisfaction guarantee graphic
• 3.Must have phone number visible
• 4. graphics offering - 1st deep clean $25 Off - 10% Off Bi Weekly Cleanings - 20% Off Weekly Cleanings
• I like the clean look of this website https://www.silverdusthouse.com/ BUT want a more compact website like https://www.brightnestcrew.com/
• Popup for when the try and x out saying Book Now And Receive $20 Off 1st Cleaning

```html
<!DOCTYPE html>
<html lang="en">
<head>
<meta charset="utf-8">
<title>Renata Sweeps – House Cleaning in Seminole County</title>
<link rel="stylesheet" href="https://fonts.googleapis.com/css2?family=Raleway:wght@500;600;700;800&family=Open+Sans:ital,wght@0,400;0,600;0,700;1,400&display=swap">
<style>
:root{
  --green:#4cb944;
  --green-dark:#3fa539;
  --blue:#2a7fd4;
  --ink:#2b2b2b;
  --muted:#6d6d6d;
  --white:#ffffff;
  --line:#d9d9d9;
}
*{box-sizing:border-box;margin:0;padding:0}
html,body{width:1200px;height:2579px;overflow:hidden}
body{position:relative;background:var(--white);font-family:"Open Sans",Arial,sans-serif;color:var(--ink)}
a{text-decoration:none;color:inherit}
.abs{position:absolute}
.heading{font-family:"Raleway",Arial,sans-serif;font-weight:700;text-transform:uppercase}

/* header */
.site-header{position:absolute;left:0;top:0;width:1200px;height:100px;background:var(--white);box-shadow:0 2px 6px rgba(0,0,0,.08);z-index:2}
.brand{position:absolute;left:98px;top:30px;display:flex;align-items:center;gap:10px;font-family:"Raleway",Arial,sans-serif;font-weight:800;font-size:27px;color:var(--blue)}
.brand-dot{width:22px;height:22px;border-radius:50%;background:var(--green)}
.main-nav{position:absolute;top:40px;left:378px;display:flex;font-family:"Raleway",Arial,sans-serif;font-weight:600;font-size:15px;color:var(--ink)}
.main-nav a{margin-right:40px}
.search-icon{position:absolute;left:842px;top:42px}
.phone-pill{position:absolute;left:888px;top:29px;width:212px;height:46px;border:1.5px solid #9a9a9a;border-radius:23px;display:flex;align-items:center;justify-content:center;gap:10px;font-weight:700;font-style:italic;font-size:19px;color:var(--ink)}

/* hero */
.hero{position:absolute;left:0;top:100px;width:1200px;height:580px;background:linear-gradient(90deg,#f4f4f2 0%,#eeeeea 45%,#d8dcd2 70%,#c7cdbf 100%)}
.hero-photo{position:absolute;left:520px;top:0;width:680px;height:580px;background:radial-gradient(ellipse at 55% 45%,#e9d9c6 0%,#b8c1d6 35%,rgba(220,224,214,0) 70%)}
.hero-title{position:absolute;left:100px;top:58px;font-size:31px;line-height:47px;color:var(--ink)}
.hero-list{position:absolute;left:100px;top:176px;list-style:none;font-size:15px;color:#3a3a3a}
.hero-list li{display:flex;align-items:center;gap:12px;height:34px}
.tick{width:15px;height:15px;border-radius:50%;background:var(--blue);display:inline-flex;align-items:center;justify-content:center;flex:none}
.btn{display:inline-flex;align-items:center;justify-content:center;background:var(--green);color:var(--white);font-family:"Raleway",Arial,sans-serif;font-weight:700;text-transform:uppercase;border-radius:26px}
.hero-btn{position:absolute;left:98px;top:368px;width:240px;height:50px;font-size:16px}
.guarantee-badge{position:absolute;left:100px;top:436px;width:98px;height:98px;border-radius:50%;background:radial-gradient(circle,#e8b317 0 55%,#c0262b 56% 68%,#e8b317 69%)}

/* welcome */
.welcome-title{position:absolute;left:0;top:763px;width:1200px;text-align:center;font-size:28px}
.welcome-text{position:absolute;left:210px;top:817px;width:780px;text-align:center;font-size:13px;line-height:24px;color:var(--muted)}
.offer{position:absolute;top:905px;width:300px;text-align:center}
.offer-icon{width:96px;height:120px;margin:0 auto;background:linear-gradient(180deg,#3d8fe0,#1f6fc4);border-radius:14px;opacity:.9}
.offer-title{margin-top:38px;font-family:"Raleway",Arial,sans-serif;font-weight:700;font-size:19px;color:var(--ink)}
.offer-text{margin-top:16px;font-size:13px;line-height:24px;color:var(--muted)}
.read-more{display:block;margin-top:18px;font-weight:700;font-size:14px;color:var(--green)}

/* pricing */
.pricing{position:absolute;left:0;top:1255px;width:1200px;height:507px;background:linear-gradient(90deg,#4e524c 0%,#6b6e64 35%,#a49a8a 55%,#cbbfae 80%,#b6a795 100%)}
.pricing-photo{position:absolute;left:500px;top:0;width:700px;height:507px;background:radial-gradient(ellipse at 45% 40%,#d9b49a 0%,#a2574f 30%,rgba(160,140,120,0) 70%)}
.pricing-title{position:absolute;left:96px;top:66px;font-size:27px;color:var(--white)}
.price-list{position:absolute;left:98px;top:126px;list-style:none;color:var(--white);font-weight:600;font-size:16px}
.price-list li{display:flex;align-items:center;height:40.5px}
.price-list .room{width:210px;display:flex;align-items:center;gap:14px}
.price-list .price{font-weight:700}
.tick-w{width:16px;height:16px;border-radius:50%;background:var(--white);display:inline-flex;align-items:center;justify-content:center}
.pricing-btn{position:absolute;left:98px;top:385px;width:157px;height:50px;font-size:16px}

/* testimonial */
.quote-badge{position:absolute;left:553px;top:1714px;width:94px;height:94px;border-radius:50%;background:var(--white);display:flex;align-items:center;justify-content:center}
.clients-title{position:absolute;left:0;top:1848px;width:1200px;text-align:center;font-size:28px}
.quote-text{position:absolute;left:230px;top:1906px;width:740px;text-align:center;font-style:italic;font-size:15px;line-height:30px;color:var(--muted)}
.quote-author{position:absolute;left:0;top:1993px;width:1200px;text-align:center;font-weight:700;font-size:15px;color:var(--blue)}
.dots{position:absolute;left:576px;top:2048px;display:flex;gap:5px}
.dots span{width:13px;height:13px;border-radius:50%;border:1.5px solid #aaa}
.dots span.on{background:#aaa}

/* footer */
.footer-shape{position:absolute;left:0;top:2150px}
.footer-brand{position:absolute;left:98px;top:2370px;display:flex;align-items:center;gap:10px;font-family:"Raleway",Arial,sans-serif;font-weight:800;font-size:32px;color:var(--white)}
.footer-brand .brand-dot{background:var(--white)}
.footer-col{position:absolute;top:2274px;color:var(--white)}
.footer-col h3{font-family:"Raleway",Arial,sans-serif;font-weight:700;font-size:17px;text-transform:uppercase;margin-bottom:24px}
.quick-links{list-style:none;font-size:12px;line-height:23px}
.news-text{font-size:12px;line-height:22px;width:215px}
.email-field{margin-top:14px;width:254px;height:33px;background:var(--white);color:#444;font-size:12px;padding:0 12px;display:flex;align-items:center}
.subscribe-btn{margin-top:18px;width:102px;height:32px;font-size:11px;border-radius:16px}
.contact-row{display:flex;gap:14px;font-size:12px;line-height:22px;margin-bottom:18px}
.contact-row svg{flex:none;margin-top:4px}
.footer-rule{position:absolute;left:98px;top:2503px;width:1004px;height:1px;background:rgba(255,255,255,.45)}
.copyright{position:absolute;left:98px;top:2528px;font-size:12px;color:var(--white)}
.socials{position:absolute;left:975px;top:2525px;display:flex;gap:8px}
.socials span{width:28px;height:28px;border-radius:50%;border:1.5px solid var(--white)}
</style>
</head>
<body>

<header class="site-header">
  <a class="brand" href="#"><span class="brand-dot"></span>Renata Sweeps</a>
  <nav class="main-nav">
    <a href="#">SERVICES</a><a href="#">CONTACT</a><a href="#">FREE ESTIMATE</a><a href="#">ABOUT</a>
  </nav>
  <svg class="search-icon" width="17" height="17" viewBox="0 0 17 17"><circle cx="7" cy="7" r="5" fill="none" stroke="#2b2b2b" stroke-width="2.2"/><path d="M11 11l4.5 4.5" stroke="#2b2b2b" stroke-width="2.4" stroke-linecap="round"/></svg>
  <a class="phone-pill" href="tel:15553180264">
    <svg width="18" height="18" viewBox="0 0 24 24"><path fill="#4cb944" d="M6.6 10.8a15.1 15.1 0 006.6 6.6l2.2-2.2c.3-.3.7-.4 1-.2 1.1.4 2.3.6 3.6.6.6 0 1 .4 1 1V20c0 .6-.4 1-1 1A17 17 0 013 4c0-.6.4-1 1-1h3.5c.6 0 1 .4 1 1 0 1.3.2 2.5.6 3.6.1.3 0 .7-.2 1z"/></svg>
    1 555 318 0264
  </a>
</header>

<section class="hero">
  <div class="hero-photo" role="img" aria-label="Smiling house cleaner in an apron holding a spray bottle and a basket of cleaning supplies"></div>
  <h1 class="heading hero-title">Cleaning Seminole County<br>Homes for over 12 Years</h1>
  <ul class="hero-list">
    <li><span class="tick"><svg width="9" height="9" viewBox="0 0 10 10"><path d="M1.5 5.2l2.3 2.3L8.5 2.8" fill="none" stroke="#fff" stroke-width="1.8"/></svg></span>Trusted by your neighbors for more than a decade</li>
    <li><span class="tick"><svg width="9" height="9" viewBox="0 0 10 10"><path d="M1.5 5.2l2.3 2.3L8.5 2.8" fill="none" stroke="#fff" stroke-width="1.8"/></svg></span>Affordable and flexible to accommodate your needs</li>
    <li><span class="tick"><svg width="9" height="9" viewBox="0 0 10 10"><path d="M1.5 5.2l2.3 2.3L8.5 2.8" fill="none" stroke="#fff" stroke-width="1.8"/></svg></span>200% Money Back Guarantee</li>
    <li><span class="tick"><svg width="9" height="9" viewBox="0 0 10 10"><path d="M1.5 5.2l2.3 2.3L8.5 2.8" fill="none" stroke="#fff" stroke-width="1.8"/></svg></span>Up to 20% Discount on Continued Cleanings</li>
    <li><span class="tick"><svg width="9" height="9" viewBox="0 0 10 10"><path d="M1.5 5.2l2.3 2.3L8.5 2.8" fill="none" stroke="#fff" stroke-width="1.8"/></svg></span>Same Day Cleanings</li>
  </ul>
  <a class="btn hero-btn" href="#">Request Free Estimate</a>
  <svg class="abs" style="left:352px;top:322px" width="80" height="108" viewBox="0 0 80 108"><path d="M52 4c26 18 20 62-22 80" fill="none" stroke="#9a9a9a" stroke-width="9" stroke-linecap="round"/><path d="M14 78l26-12-8 30z" fill="#9a9a9a"/></svg>
  <div class="guarantee-badge" role="img" aria-label="200% satisfaction guaranteed seal"></div>
</section>

<section>
  <h2 class="heading welcome-title">Welcome to Renata Sweeps</h2>
  <p class="welcome-text">At vero eos et accusamus et iusto odio dignissimos ducimus qui blanditiis praesentium voluptatum deleniti atque corrupti quos dolores et quas molestias excepturi sint occaecati cupiditate milique sunt in culpa qui officia deserunt mollit</p>

  <div class="offer" style="left:81px">
    <div class="offer-icon" role="img" aria-label="Feather duster icon"></div>
    <h3 class="offer-title">1st deep clean $25 Off</h3>
    <p class="offer-text">Nam libero tempore, cum soluta nobis est eli<br>gendi optio cumque nihil impedit</p>
    <a class="read-more" href="#">READ MORE &gt;&gt;</a>
  </div>
  <div class="offer" style="left:449px">
    <div class="offer-icon" role="img" aria-label="Mop and cleaning bottles icon"></div>
    <h3 class="offer-title">10% Off Bi Weekly Cleanings</h3>
    <p class="offer-text">Nam libero tempore, cum soluta nobis est eli<br>gendi optio cumque nihil impedit</p>
    <a class="read-more" href="#">READ MORE &gt;&gt;</a>
  </div>
  <div class="offer" style="left:816px">
    <div class="offer-icon" role="img" aria-label="Bucket with soap foam icon"></div>
    <h3 class="offer-title">20% Off Weekly Cleanings</h3>
    <p class="offer-text">Nam libero tempore, cum soluta nobis est eli<br>gendi optio cumque nihil impedit</p>
    <a class="read-more" href="#">READ MORE &gt;&gt;</a>
  </div>
</section>

<section class="pricing">
  <div class="pricing-photo" role="img" aria-label="Smiling woman in yellow gloves wiping a table with a cloth"></div>
  <h2 class="heading pricing-title">Pricing Plan</h2>
  <ul class="price-list">
    <li><span class="room"><span class="tick-w"><svg width="9" height="9" viewBox="0 0 10 10"><path d="M1.5 5.2l2.3 2.3L8.5 2.8" fill="none" stroke="#555" stroke-width="1.8"/></svg></span>One bedroom home</span><span class="price">$85</span></li>
    <li><span class="room"><span class="tick-w"><svg width="9" height="9" viewBox="0 0 10 10"><path d="M1.5 5.2l2.3 2.3L8.5 2.8" fill="none" stroke="#555" stroke-width="1.8"/></svg></span>Two bedroom home</span><span class="price">$90</span></li>
    <li><span class="room"><span class="tick-w"><svg width="9" height="9" viewBox="0 0 10 10"><path d="M1.5 5.2l2.3 2.3L8.5 2.8" fill="none" stroke="#555" stroke-width="1.8"/></svg></span>Three bedroom home</span><span class="price">$105</span></li>
    <li><span class="room"><span class="tick-w"><svg width="9" height="9" viewBox="0 0 10 10"><path d="M1.5 5.2l2.3 2.3L8.5 2.8" fill="none" stroke="#555" stroke-width="1.8"/></svg></span>Four bedroom home</span><span class="price">$120</span></li>
    <li><span class="room"><span class="tick-w"><svg width="9" height="9" viewBox="0 0 10 10"><path d="M1.5 5.2l2.3 2.3L8.5 2.8" fill="none" stroke="#555" stroke-width="1.8"/></svg></span>Five bedroom home</span><span class="price">$150</span></li>
    <li><span class="room"><span class="tick-w"><svg width="9" height="9" viewBox="0 0 10 10"><path d="M1.5 5.2l2.3 2.3L8.5 2.8" fill="none" stroke="#555" stroke-width="1.8"/></svg></span>Six bedroom home</span><span class="price">$200</span></li>
  </ul>
  <a class="btn pricing-btn" href="#">Get Started</a>
</section>

<section>
  <div class="quote-badge">
    <svg width="40" height="32" viewBox="0 0 40 32"><path fill="#4cb944" d="M2 14C2 6 6 2 13 1v5c-4 1-5 3-5 7h5v17H2zM23 14c0-8 4-12 11-13v5c-4 1-5 3-5 7h5v17H23z"/></svg>
  </div>
  <h2 class="heading clients-title">My Clients Are Happy</h2>
  <p class="quote-text">"Renata has been cleaning my home for the past 3 1/2 years and I couldn't be happier with her. I trust her with cleaning my home while I'm out of town and recommend her to my friends."</p>
  <p class="quote-author">- JOHN DOE</p>
  <div class="dots"><span class="on"></span><span></span><span></span></div>
</section>

<footer>
  <svg class="footer-shape" width="1200" height="429" viewBox="0 0 1200 429">
    <path d="M0 102Q600-92 1200 102V429H0Z" fill="#2a7fd4"/>
    <path d="M0 98Q600-98 1200 98" fill="none" stroke="#4cb944" stroke-width="7"/>
  </svg>
  <a class="footer-brand" href="#"><span class="brand-dot"></span>Renata Sweeps</a>

  <div class="footer-col" style="left:410px">
    <h3>Quick Links</h3>
    <ul class="quick-links">
      <li>About us</li><li>FAQ</li><li>Sitemap</li><li>Terms &amp; Conditions</li><li>Privacy Policy</li><li>Contact Us</li>
    </ul>
  </div>

  <div class="footer-col" style="left:602px">
    <h3>Newsletter Subscription</h3>
    <p class="news-text">Register your Email Address to get Information about us</p>
    <div class="email-field">Email Address</div>
    <a class="btn subscribe-btn" href="#">Subscribe</a>
  </div>

  <div class="footer-col" style="left:947px">
    <h3>Contact Us</h3>
    <div class="contact-row"><svg width="11" height="14" viewBox="0 0 11 14"><path fill="#fff" d="M5.5 0A5.5 5.5 0 000 5.5C0 9.5 5.5 14 5.5 14S11 9.5 11 5.5A5.5 5.5 0 005.5 0zm0 7.5a2 2 0 110-4 2 2 0 010 4z"/></svg><span>Renata Sweeps<br>Dana Whitmore, MBA<br>President</span></div>
    <div class="contact-row"><svg width="13" height="13" viewBox="0 0 24 24"><path fill="#fff" d="M6.6 10.8a15.1 15.1 0 006.6 6.6l2.2-2.2c.3-.3.7-.4 1-.2 1.1.4 2.3.6 3.6.6.6 0 1 .4 1 1V20c0 .6-.4 1-1 1A17 17 0 013 4c0-.6.4-1 1-1h3.5c.6 0 1 .4 1 1 0 1.3.2 2.5.6 3.6.1.3 0 .7-.2 1z"/></svg><span>+1 555 318 0264</span></div>
    <div class="contact-row"><svg width="14" height="11" viewBox="0 0 14 11"><path fill="#fff" d="M0 0h14v11H0z"/><path d="M0 0l7 6 7-6" fill="none" stroke="#2a7fd4" stroke-width="1.4"/></svg><span>info@renatasweeps.com</span></div>
  </div>

  <div class="footer-rule"></div>
  <p class="copyright">Copyrights © 2017, Renata Sweeps. All rights reserved.</p>
  <div class="socials"><span></span><span></span><span></span><span></span></div>
</footer>

</body>
</html>
```